Kelvane Plumbing Business cards

Company is Kelvane Plumbing.
name Dashel Morrowby, I am a plumber, drainer, gasfitter and roofer
Mobile: 0431 906 154
Email address: info@kelvaneplumbing.example (check out my website for some ideas)
Website: www.kelvaneplumbing.example
ABN: 82 916 203 471
LIC: 604517K

I am reliable all round plumber. I am a 24 hour emergency service. Kelvane Plumbing is a professional plumbing service in the Illawarra, South Coast, Southern Sydney and Southern Highland regions of NSW. We offer a 24 hour emergency service for piece of mind to our customers. Call us now to see how we can help you. Kelvane Plumbing approaches every job with attention to detail and excellent customer service. With our superior workmanship you can be confident that the job will be done right the first time around. You can rest assured with results that are guaranteed to last.

Target Market(s)

the general public

Contact Information for Business Card

look up website for some ideas something with similar colours to logo and new modern and to catch the eye.

Colors
fdfdfd
ffffff
000000
7f7f7f
aaaaaa
33a6d7
0492cd

Requirements
Must have
• all contact details
• company- Kelvane Plumbing
• name- Dashel Morrowby
• number mobile- 0431 906 154
• Email address- info@kelvaneplumbing.example
• Website- www.kelvaneplumbing.example
• ABN- 82 916 203 471
• LIC- 604517K

```html
<!DOCTYPE html>
<html lang="en">
<head>
<meta charset="utf-8">
<title>Kelvane Plumbing – Business Cards</title>
<link rel="stylesheet" href="https://fonts.googleapis.com/css2?family=Barlow:wght@400;500;600&family=Barlow+Semi+Condensed:wght@400;500&display=swap">
<style>
  :root {
    --stage: #e4e4e4;
    --ink: #050708;
    --paper: #ffffff;
    --brand-blue: #1a9bcb;
    --deep-blue: #0492cd;
    --grey: #7f7f7f;
  }
  * { margin: 0; padding: 0; box-sizing: border-box; }
  html, body { width: 1200px; height: 1200px; overflow: hidden; }
  body {
    background: var(--stage);
    font-family: "Barlow", sans-serif;
    position: relative;
  }
  .card { position: absolute; overflow: hidden; }

  /* Front */
  .card-front {
    left: 261px; top: 169px; width: 667px; height: 381px;
    background: var(--ink);
  }
  .brand-mark {
    position: absolute; left: 0; right: 0; text-align: center;
    font-family: "Barlow", sans-serif; font-weight: 600;
    color: var(--brand-blue); letter-spacing: 0.5px;
  }
  .card-front .brand-mark { top: 158px; font-size: 34px; }
  .front-url {
    position: absolute; left: 0; right: 0; top: 292px; text-align: center;
    font-family: "Barlow Semi Condensed", sans-serif; font-size: 17px;
    color: var(--brand-blue);
  }

  /* Back */
  .card-back {
    left: 260px; top: 654px; width: 668px; height: 383px;
    background: var(--paper);
  }
  .card-back .brand-mark { left: 0; width: 332px; top: 172px; font-size: 28px; }
  .reg-details {
    position: absolute; top: 340px; font-size: 15px; color: var(--brand-blue);
    font-family: "Barlow Semi Condensed", sans-serif;
  }
  .reg-details b { font-weight: 500; }
  .reg-abn { left: 22px; }
  .reg-lic { left: 216px; }

  .contact-panel {
    position: absolute; left: 332px; top: 0; width: 336px; height: 383px;
    background: var(--brand-blue); color: var(--paper);
  }
  .panel-notch {
    position: absolute; left: 328px; top: 146px; width: 4px; height: 90px;
    background: var(--brand-blue);
  }
  .company-name {
    position: absolute; right: 27px; top: 22px;
    font-size: 31px; font-weight: 500; letter-spacing: 0.3px;
    padding-bottom: 2px; border-bottom: 1px solid var(--paper);
    white-space: nowrap;
  }
  .person-name {
    position: absolute; right: 27px; top: 64px;
    font-family: "Barlow Semi Condensed", sans-serif; font-size: 16px;
  }
  .contact-list { position: absolute; right: 27px; top: 242px; list-style: none; }
  .contact-list li {
    display: flex; justify-content: flex-end; align-items: center;
    height: 25px; margin-bottom: 12.5px; font-size: 18px; gap: 4px;
  }
  .contact-icon { width: 25px; height: 25px; flex: none; }
</style>
</head>
<body>
  <section class="card card-front">
    <div class="brand-mark">Kelvane Plumbing</div>
    <div class="front-url">www.kelvaneplumbing.example</div>
  </section>

  <section class="card card-back">
    <div class="brand-mark">Kelvane Plumbing</div>
    <p class="reg-details reg-abn"><b>ABN:</b> 82 916 203 471</p>
    <p class="reg-details reg-lic"><b>LIC:</b> 604517K</p>

    <div class="panel-notch"></div>
    <div class="contact-panel">
      <h1 class="company-name">Kelvane Plumbing</h1>
      <p class="person-name">Dashel Morrowby</p>
      <ul class="contact-list">
        <li>0431 906 154
          <svg class="contact-icon" viewBox="0 0 24 24" aria-hidden="true">
            <circle cx="12" cy="12" r="12" fill="#fff"/>
            <path d="M6 10c0-2 3-3.5 6-3.5s6 1.5 6 3.5h-3v-1.5h-6V10z" fill="#1a9bcb"/>
            <rect x="7.5" y="11" width="9" height="6" rx="1" fill="#1a9bcb"/>
            <circle cx="12" cy="14" r="1.6" fill="#fff"/>
          </svg>
        </li>
        <li>info@kelvaneplumbing.example
          <svg class="contact-icon" viewBox="0 0 24 24" aria-hidden="true">
            <circle cx="12" cy="12" r="12" fill="#fff"/>
            <rect x="6" y="8" width="12" height="8.5" rx="1" fill="#1a9bcb"/>
            <path d="M6.5 8.8l5.5 4 5.5-4" stroke="#fff" stroke-width="1.2" fill="none"/>
          </svg>
        </li>
        <li>www.kelvaneplumbing.example
          <svg class="contact-icon" viewBox="0 0 24 24" aria-hidden="true">
            <circle cx="12" cy="12" r="12" fill="#fff"/>
            <g stroke="#1a9bcb" stroke-width="1.2" fill="none">
              <circle cx="12" cy="12" r="6.5"/>
              <ellipse cx="12" cy="12" rx="3" ry="6.5"/>
              <path d="M5.5 12h13M6.5 9h11M6.5 15h11"/>
            </g>
          </svg>
        </li>
      </ul>
    </div>
  </section>
</body>
</html>
```